Marlow Hire Business Card for recruitment company

We are looking for a Business Card Design that incorporates our personal details and our busines name and logo. We are a specialized search consultancy that recruit Property and Construction professionals.
We would like a business card that stands out and is appealing to the Construction and Property industry as well.

Target Market(s)

people in the construction and property industry

Contact Information for Business Card

Business Name and logo

Font styles to use
Serif

Colors
0094D4
00A9DD
6FCCEA
C7EBF8
E9F6FB

Requirements
Must have
• Business name and logo as well as contact details
Should not have
• No photos of us please

```html
<!DOCTYPE html>
<html lang="en">
<head>
<meta charset="utf-8">
<title>Marlow Hire – Business Card</title>
<link href="https://fonts.googleapis.com/css2?family=Rokkitt:wght@400;500;600&display=swap" rel="stylesheet">
<style>
  :root {
    --backdrop: #d8d7d4;
    --card-teal: #4a898a;
    --ink-navy: #1c3954;
  }
  * { margin: 0; padding: 0; box-sizing: border-box; }
  html, body {
    width: 1200px;
    height: 800px;
    overflow: hidden;
    background: var(--backdrop);
  }
  .canvas {
    position: relative;
    width: 1200px;
    height: 800px;
  }
  .card {
    position: absolute;
    left: 374px;
    width: 451px;
    height: 281px;
    background: var(--card-teal);
    color: var(--ink-navy);
    font-family: "Rokkitt", Georgia, serif;
    text-align: center;
  }
  .card--front { top: 87px; }
  .card--back { top: 431px; }

  .brand-name {
    position: absolute;
    left: 0;
    right: 0;
    top: 112px;
    font-size: 46px;
    font-weight: 500;
    letter-spacing: 2px;
    text-transform: uppercase;
    line-height: 1;
  }

  .holder-name {
    position: absolute;
    left: 0;
    right: 0;
    top: 78px;
    font-size: 29px;
    font-weight: 600;
    letter-spacing: 2px;
    line-height: 1;
  }
  .holder-role {
    position: absolute;
    left: 0;
    right: 0;
    top: 108px;
    font-size: 15.5px;
    font-weight: 500;
    letter-spacing: 0.6px;
  }
  .contact-list {
    position: absolute;
    left: 0;
    right: 0;
    top: 153px;
    list-style: none;
    font-size: 14px;
    font-weight: 500;
    letter-spacing: 0.5px;
    line-height: 20px;
  }
</style>
</head>
<body>
  <main class="canvas">
    <section class="card card--front" aria-label="Card front">
      <h1 class="brand-name">Marlow Hire</h1>
    </section>

    <section class="card card--back" aria-label="Card back">
      <h2 class="holder-name">Helena Rowe</h2>
      <p class="holder-role">Director | Senior Search Consultant</p>
      <ul class="contact-list">
        <li class="contact-phone">+64 27 404 2291</li>
        <li class="contact-email">helena@marlowhire.nz</li>
        <li class="contact-web">www.marlowhire.nz</li>
      </ul>
    </section>
  </main>
</body>
</html>
```